Stationary Design for Stunning new Logo

I need to envelopes, letterhead, business cards designed to compliment our new logo.

We are a 25 year old printing company going through a brand refresh. All items should have the design extended to both sides for full print ability.

Industry/Entity Type

Printing

Requirements
Must have
• It must utilize the new logo & colors PMS 300 & PMS 295.

```html
<!DOCTYPE html>
<html lang="en">
<head>
<meta charset="utf-8">
<title>Pressline Business Cards</title>
<link href="https://fonts.googleapis.com/css2?family=Open+Sans:wght@400;600;800&display=swap" rel="stylesheet">
<style>
  :root {
    --pms-300: #005eb8;
    --pms-295: #00386b;
    --ink: #3a3d42;
    --paper: #ffffff;
    --backdrop: #e9ebee;
  }
  * { box-sizing: border-box; margin: 0; padding: 0; }
  html, body { width: 1200px; height: 720px; overflow: hidden; }
  body {
    background: var(--backdrop);
    font-family: "Open Sans", Arial, sans-serif;
    position: relative;
  }
  .card {
    position: absolute;
    top: 205px;
    width: 540px;
    height: 309px;
    background: var(--paper);
    box-shadow: 0 6px 18px rgba(0,0,0,0.12);
  }
  .card--front { left: 40px; }
  .card--back { left: 620px; }

  .brand { display: flex; align-items: center; gap: 10px; }
  .brand__dot {
    width: 30px; height: 30px; border-radius: 50%;
    background: var(--pms-300);
    flex: none;
  }
  .brand__name {
    font-weight: 800;
    color: var(--pms-300);
    letter-spacing: 1px;
    line-height: 1;
    white-space: nowrap;
  }

  .card--front .brand { position: absolute; left: 34px; top: 34px; }
  .card--front .brand__name { font-size: 44px; }

  .holder {
    position: absolute; left: 34px; top: 124px;
    font-size: 17px; font-weight: 600; color: var(--pms-300);
  }
  .holder__title { font-size: 12px; font-weight: 400; }

  .contacts { position: absolute; left: 34px; top: 156px; list-style: none; }
  .contacts li {
    display: flex; align-items: center; gap: 8px;
    font-size: 13px; color: var(--ink); height: 22px;
  }
  .contacts svg { width: 12px; height: 12px; fill: var(--pms-300); flex: none; }
  .address {
    position: absolute; left: 54px; top: 256px;
    font-size: 13px; color: var(--ink);
  }

  .card--back .brand { position: absolute; right: 40px; top: 96px; }
  .card--back .brand__name { font-size: 52px; }
  .web {
    position: absolute; right: 40px; bottom: 40px;
    font-size: 15px; letter-spacing: 1.5px; color: var(--ink);
  }
  .web__name { color: var(--pms-300); }
</style>
</head>
<body>
  <section class="card card--front">
    <div class="brand">
      <span class="brand__dot"></span>
      <span class="brand__name">PRESSLINE</span>
    </div>

    <div class="holder">Your Name, <span class="holder__title">Title</span></div>

    <ul class="contacts">
      <li>
        <svg viewBox="0 0 24 24" aria-hidden="true"><path d="M6.6 10.8a15 15 0 0 0 6.6 6.6l2.2-2.2a1 1 0 0 1 1-.25 11.4 11.4 0 0 0 3.6.57 1 1 0 0 1 1 1V20a1 1 0 0 1-1 1A17 17 0 0 1 3 4a1 1 0 0 1 1-1h3.5a1 1 0 0 1 1 1c0 1.25.2 2.45.57 3.6a1 1 0 0 1-.25 1z"/></svg>
        123-456-789
      </li>
      <li>
        <svg viewBox="0 0 24 24" aria-hidden="true"><circle cx="12" cy="7" r="5"/><path d="M2 22c0-5.5 4.5-9 10-9s10 3.5 10 9z"/></svg>
        456-789-123
      </li>
      <li>
        <svg viewBox="0 0 24 24" aria-hidden="true"><path d="M2 5h20v14H2z M2 5l10 8 10-8" /></svg>
        hello@pressline.com
      </li>
      <li>
        <svg viewBox="0 0 24 24" aria-hidden="true"><path d="M12 2a10 10 0 1 0 0 20 10 10 0 0 0 0-20zm6.9 6h-3a15 15 0 0 0-1.3-3.9A8 8 0 0 1 18.9 8zM12 4c.8 1.2 1.5 2.5 1.9 4h-3.8c.4-1.5 1.1-2.8 1.9-4zM4.3 14a8 8 0 0 1 0-4h3.4a16 16 0 0 0 0 4zm.8 2h3a15 15 0 0 0 1.3 3.9A8 8 0 0 1 5.1 16zm3-8h-3a8 8 0 0 1 4.3-3.9A15 15 0 0 0 8.1 8zM12 20c-.8-1.2-1.5-2.5-1.9-4h3.8c-.4 1.5-1.1 2.8-1.9 4zm2.3-6H9.7a14 14 0 0 1 0-4h4.6a14 14 0 0 1 0 4zm.3 5.9a15 15 0 0 0 1.3-3.9h3a8 8 0 0 1-4.3 3.9zm1.7-5.9a16 16 0 0 0 0-4h3.4a8 8 0 0 1 0 4z"/></svg>
        www.pressline.com
      </li>
    </ul>

    <p class="address">00, Complex name, street, city 00423</p>
  </section>

  <section class="card card--back">
    <div class="brand">
      <span class="brand__dot"></span>
      <span class="brand__name">PRESSLINE</span>
    </div>
    <p class="web">www.<span class="web__name">pressline</span>.com</p>
  </section>
</body>
</html>
```